ready mix concrete business

i need a logo for a ready mix company
it is called Pine Hollow Concrete for business cards and promotional items. would like a ready mix truck on it
and must look profesional

```html
<!DOCTYPE html>
<html lang="en">
<head>
<meta charset="utf-8">
<title>Pine Hollow Concrete – Business Card</title>
<link href="https://fonts.googleapis.com/css2?family=Montserrat:wght@400;700&display=swap" rel="stylesheet">
<style>
  :root {
    --card-white: #ffffff;
    --brand-red: #c6202e;
    --band-grey: #9c9c9e;
    --ink-dark: #1f1f1f;
    --text-light: #ffffff;
    --page-bg: #ececec;
  }
  * { box-sizing: border-box; margin: 0; padding: 0; }
  html, body {
    width: 1200px; height: 720px; overflow: hidden;
    background: var(--page-bg);
    font-family: "Montserrat", Arial, sans-serif;
  }
  .card {
    position: relative;
    width: 1200px; height: 720px;
    background: var(--card-white);
    overflow: hidden;
  }
  .brand {
    position: absolute;
    top: 150px; left: 0; width: 100%;
    display: flex; align-items: center; justify-content: center; gap: 22px;
  }
  .brand-mark {
    width: 46px; height: 46px; border-radius: 50%;
    background: var(--brand-red);
  }
  .brand-name {
    font-weight: 700; font-size: 52px; letter-spacing: 1px;
    color: var(--ink-dark); text-transform: uppercase;
  }
  .name-panel {
    position: absolute;
    left: 0; top: 340px; width: 640px; height: 115px;
    background: var(--band-grey);
    color: var(--text-light);
    padding: 22px 0 0 150px;
  }
  .person-name { font-size: 36px; font-weight: 400; letter-spacing: 1px; }
  .person-role { font-size: 18px; margin-top: 2px; padding-left: 40px; }
  .contact-panel {
    position: absolute;
    left: 665px; top: 275px; width: 535px; height: 180px;
    background: var(--band-grey);
    color: var(--text-light);
    padding: 26px 0 0 60px;
    list-style: none;
  }
  .contact-item {
    display: flex; align-items: center; gap: 18px;
    font-size: 20px; height: 40px;
  }
  .contact-icon { width: 26px; height: 26px; flex: none; }
  .info-band {
    position: absolute;
    left: 0; top: 455px; width: 100%; height: 125px;
    background: var(--brand-red);
    color: var(--text-light);
    text-align: center;
    padding-top: 14px;
  }
  .address { font-size: 22px; letter-spacing: 0.5px; }
  .website { font-size: 34px; margin-top: 10px; letter-spacing: 0.5px; }
  .rule-band {
    position: absolute;
    left: 0; top: 606px; width: 100%; height: 58px;
    background: var(--brand-red);
  }
</style>
</head>
<body>
  <main class="card">
    <header class="brand">
      <span class="brand-mark"></span>
      <span class="brand-name">Pine Hollow Concrete</span>
    </header>

    <section class="name-panel">
      <p class="person-name">YOUR NAME</p>
      <p class="person-role">Post</p>
    </section>

    <ul class="contact-panel">
      <li class="contact-item">
        <svg class="contact-icon" viewBox="0 0 24 24" aria-hidden="true">
          <circle cx="12" cy="12" r="11" fill="none" stroke="#fff" stroke-width="1.6"/>
          <path d="M8 6.5l2 2.5-1.2 1.4c.8 1.7 2 2.9 3.8 3.8l1.4-1.2 2.5 2-1.2 2.2C11 16.9 7.1 13 6.3 8z" fill="#fff"/>
        </svg>
        <span>123 456 7890</span>
      </li>
      <li class="contact-item">
        <svg class="contact-icon" viewBox="0 0 24 24" aria-hidden="true">
          <circle cx="12" cy="12" r="12" fill="#fff"/>
          <path d="M8 6.5l2 2.5-1.2 1.4c.8 1.7 2 2.9 3.8 3.8l1.4-1.2 2.5 2-1.2 2.2C11 16.9 7.1 13 6.3 8z" fill="#9c9c9e"/>
        </svg>
        <span>123 456 7890</span>
      </li>
      <li class="contact-item">
        <svg class="contact-icon" viewBox="0 0 24 24" aria-hidden="true">
          <rect x="3" y="6" width="18" height="12" fill="#fff"/>
          <path d="M3 6l9 7 9-7" fill="none" stroke="#9c9c9e" stroke-width="1.5"/>
        </svg>
        <span>yourmail@mailbox.com</span>
      </li>
    </ul>

    <section class="info-band">
      <p class="address">1234, Street name, Area</p>
      <p class="website">yourwebsite.com</p>
    </section>

    <div class="rule-band"></div>
  </main>
</body>
</html>
```